Current website re-design to a updated look and feel.

We currently have a website www.brightlanefreight.com that we want to give an updated look and feel to. We are a logistics company that competes with Harbex, Dm Whitfield, Tarn but on a smaller scale. We want something fresh and updated. We have two locations one in downtown Chicago, IL and one in Palatine IL. We are a fun group that also gets the job done. We know we need pictures of both locations and possibly a video, but we need fresh design ideas. The 'who we are' page is really the only page that we currently want to keep. The 'what we do' page needs to be completely re-done from a look and feel for sure.

Target Market(s)

Anyone who uses Truck transportation to move their product. Mainly US manufacturers.

Industry/Entity Type

Logistics

Number of Pages Required

5+ page

Font styles to use
Sans Serif

Colors
5c91c4
0355a3
d0dfed

Requirements
Must have
• The new design must entice people to want to do business with us. The design must have locations for pictures and at least one video which we know we will have to provide. Design must be easy to navigate.

```html
<!DOCTYPE html>
<html lang="en">
<head>
<meta charset="utf-8">
<title>Get Updates – Brightlane Freight</title>
<link rel="stylesheet" href="https://fonts.googleapis.com/css2?family=Montserrat:wght@600;700&family=Raleway:wght@300;400&display=swap">
<style>
  :root{
    --brand-deep:#0355a3;
    --brand-mid:#5c91c4;
    --brand-pale:#d0dfed;
    --panel:#f6f6f7;
    --white:#ffffff;
    --ink:#222222;
    --muted:#6d6d6d;
    --field-line:#b9b9bd;
    --night:#0c1f4d;
  }
  *{box-sizing:border-box;margin:0;padding:0}
  html,body{width:1200px;height:1200px;overflow:hidden;background:var(--white)}
  .page{position:relative;width:1200px;height:1200px;font-family:"Raleway",sans-serif}
  .fleet-photo{position:absolute;left:244px;top:36px;width:720px;height:210px;
    background:linear-gradient(90deg,#c9cbcf 0%,#e4e5e8 22%,#2f6fe0 38%,#2a62d4 62%,#e4e5e8 78%,#c9cbcf 100%);
    border-radius:40px 40px 0 0}
  .signup-panel{position:absolute;left:14px;top:246px;width:1172px;height:856px;background:var(--panel)}
  .world-map{position:absolute;left:0;top:100px;width:1172px;height:760px;
    background:radial-gradient(ellipse at 50% 45%,rgba(208,223,237,.25),rgba(246,246,247,0) 70%)}
  .mail-icon{position:absolute;left:546px;top:64px}
  .title{position:absolute;left:0;width:1172px;top:165px;text-align:center;
    font-family:"Montserrat",sans-serif;font-weight:700;font-size:32px;letter-spacing:1.4px;color:var(--brand-deep)}
  .title-rule{position:absolute;left:514px;top:216px;width:144px;height:2px;background:#e6e6e8}
  .intro{position:absolute;left:301px;top:250px;width:620px;font-size:18px;letter-spacing:.4px;font-weight:300;line-height:28px;color:var(--muted)}
  .intro strong{font-family:"Montserrat",sans-serif;font-weight:700;letter-spacing:0;color:var(--ink)}
  .field{position:absolute;left:309px;width:555px;height:60px;background:var(--white);
    border:1px solid var(--field-line);border-radius:6px;padding-left:18px;
    display:flex;align-items:center;font-size:16.5px;font-weight:300;letter-spacing:.3px;color:var(--muted)}
  .field.is-filled{font-family:"Montserrat",sans-serif;font-weight:600;letter-spacing:0;font-size:17px;color:var(--brand-deep)}
  .caret{display:inline-block;width:1px;height:18px;background:#999;margin-left:9px}
  .signup-btn{position:absolute;left:312px;top:714px;width:291px;height:59px;border-radius:6px;
    background:linear-gradient(180deg,#1c86cc 0%,#0c4fae 100%);color:var(--white);
    font-family:"Montserrat",sans-serif;font-weight:700;font-size:21px;letter-spacing:1.5px;
    display:flex;align-items:center;justify-content:center}
  .night-band{position:absolute;left:14px;top:1102px;width:1172px;height:98px;
    background:linear-gradient(90deg,#0b1a45 0%,#0f2a66 55%,#1f5f98 100%)}
  .content-card{position:absolute;left:124px;top:1160px;width:952px;height:40px;background:var(--white);
    border:5px solid #1a8ad4;border-bottom:none}
</style>
</head>
<body>
<div class="page">
  <div class="fleet-photo" role="img" aria-label="Front view of a row of trucks with a blue cab in the centre"></div>

  <section class="signup-panel">
    <div class="world-map" role="img" aria-label="Faint dotted world map in the background"></div>

    <svg class="mail-icon" width="80" height="80" viewBox="0 0 80 80" aria-hidden="true">
      <defs><linearGradient id="ring" x1="0" y1="0" x2="0" y2="1"><stop offset="0" stop-color="#1c86cc"/><stop offset="1" stop-color="#0b3f9e"/></linearGradient></defs>
      <circle cx="40" cy="40" r="38.5" fill="#fff" stroke="url(#ring)" stroke-width="2"/>
      <circle cx="38" cy="40" r="20" fill="none" stroke="#0355a3" stroke-width="1.2" stroke-dasharray="1.5 2.5"/>
      <rect x="18" y="28" width="36" height="24" rx="2" fill="#fff" stroke="#0355a3" stroke-width="2"/>
      <path d="M18 29 L36 42 L54 29" fill="none" stroke="#0355a3" stroke-width="2"/>
      <circle cx="49" cy="44" r="7" fill="#fff" stroke="#0355a3" stroke-width="1.6"/>
      <text x="49" y="48" text-anchor="middle" font-family="Montserrat,sans-serif" font-size="10" font-weight="700" fill="#0355a3">@</text>
      <path d="M56 31 H63 M58 35 H63" stroke="#0355a3" stroke-width="1.6"/>
    </svg>

    <h2 class="title">GET UPDATES</h2>
    <div class="title-rule"></div>

    <p class="intro">We occasionally send out news and related industry articles.<br><strong>Sign up</strong> and we promise to deliver quality information to you.</p>

    <div class="field is-filled" style="top:353px">Maren Lee<span class="caret"></span></div>
    <div class="field" style="top:443px">Last Name</div>
    <div class="field" style="top:533px">Organization</div>
    <div class="field" style="top:624px">Email</div>
    <div class="signup-btn">SIGN UP</div>
  </section>

  <div class="night-band" role="img" aria-label="Dark blue photo of a truck cab at night"></div>
  <div class="content-card"></div>
</div>
</body>
</html>
```